Mirvane Trinkets
Lucinda Harrow Designs
Mirvane Trinkets -
Creative Brief
Simple
Lucinda Harrow
Jewelry Designer
2719 Quillfern Ln Dallas TX 75294
lucinda@mirvane-example.com
www.mirvane-example.com
Please do a few designs!
Maybe just the logo?

```html
<!DOCTYPE html>
<html lang="en">
<head>
<meta charset="utf-8">
<title>Mirvane Trinkets – Business Cards</title>
<link href="https://fonts.googleapis.com/css2?family=Arimo:wght@400;700&display=swap" rel="stylesheet">
<style>
  :root {
    --backdrop: #4a4a4a;
    --teal: #1d5c55;
    --teal-dark: #16463f;
    --ink: #3b3b3b;
    --grey: #6f6f6f;
    --rule: #2e2e2e;
    --paper: #ffffff;
  }
  html, body {
    margin: 0;
    padding: 0;
    width: 1200px;
    height: 804px;
    overflow: hidden;
    background: var(--backdrop);
    font-family: "Arimo", Arial, sans-serif;
  }
  .canvas {
    position: relative;
    width: 1200px;
    height: 804px;
  }
  .card {
    position: absolute;
    border-radius: 14px;
    overflow: hidden;
    box-shadow: 0 6px 18px rgba(0,0,0,0.35);
  }
  .card--front {
    left: 331px; top: 115px; width: 533px; height: 274px;
    background: var(--paper);
  }
  .card--back-light {
    left: 94px; top: 420px; width: 463px; height: 269px;
    background: var(--paper);
  }
  .card--back-teal {
    left: 576px; top: 420px; width: 461px; height: 269px;
    background: var(--teal);
  }
  .swoosh {
    position: absolute;
    inset: 0;
  }
  .brand {
    position: absolute;
    display: flex;
    flex-direction: column;
    align-items: center;
  }
  .brand__dot {
    width: 34px;
    height: 34px;
    border-radius: 50%;
    background: #9a9a9a;
    margin-bottom: 10px;
  }
  .brand__name {
    font-weight: 400;
    color: var(--ink);
    letter-spacing: 1px;
    white-space: nowrap;
  }
  .card--front .brand { left: 28px; top: 52px; }
  .card--front .brand__name { font-size: 22px; }
  .card--back-light .brand { left: 0; right: 0; top: 62px; }
  .card--back-light .brand__name { font-size: 34px; }
  .card--back-teal .brand { left: 0; right: 0; top: 62px; }
  .card--back-teal .brand__dot { background: #2f2f2f; }
  .card--back-teal .brand__name { font-size: 34px; color: #2a2f2e; }

  .contact {
    position: absolute;
    left: 252px;
    top: 52px;
    font-size: 12px;
    color: var(--ink);
    line-height: 1.35;
  }
  .contact__name {
    font-size: 16px;
    font-weight: 700;
    color: var(--teal);
  }
  .contact__title {
    font-size: 11px;
    color: var(--grey);
    margin-bottom: 28px;
  }
  .contact__label {
    font-weight: 700;
    color: var(--teal);
  }
  .contact__label--email { font-size: 15px; }
  .url {
    position: absolute;
    font-size: 13px;
  }
  .card--front .url { right: 26px; bottom: 14px; color: var(--paper); }
  .card--back-light .url { left: 0; right: 0; bottom: 22px; text-align: center; color: var(--teal); }
</style>
</head>
<body>
<main class="canvas">

  <section class="card card--front">
    <svg class="swoosh" viewBox="0 0 533 274" width="533" height="274" aria-hidden="true">
      <path d="M0 152 C120 250 330 232 533 192 L533 274 L0 274 Z" fill="var(--teal)"/>
      <path d="M0 140 C130 238 330 218 533 178" fill="none" stroke="var(--rule)" stroke-width="4"/>
    </svg>
    <div class="brand">
      <span class="brand__dot"></span>
      <span class="brand__name">Mirvane Trinkets</span>
    </div>
    <div class="contact">
      <div class="contact__name">Lucinda Harrow</div>
      <div class="contact__title">Jewelry Designer</div>
      <div>2719 Quillfern Ln</div>
      <div>Dallas TX 75294</div>
      <div><span class="contact__label">Phone</span> 214-555-0139</div>
      <div><span class="contact__label contact__label--email">Email</span> lucinda@mirvane-example.com</div>
    </div>
    <div class="url">www.mirvane-example.com</div>
  </section>

  <section class="card card--back-light">
    <div class="brand">
      <span class="brand__dot"></span>
      <span class="brand__name">Mirvane Trinkets</span>
    </div>
    <div class="url">www.mirvane-example.com</div>
  </section>

  <section class="card card--back-teal">
    <div class="brand">
      <span class="brand__dot"></span>
      <span class="brand__name">Mirvane Trinkets</span>
    </div>
  </section>

</main>
</body>
</html>
```